FRONT OF HOUSE SHOP SIGNAGE - SIGN SHOP

We have a large shop front area where we are wanting to install new signage which which communicates to our passing customers what type of signage we do and what prices we charge. I started the design but ran out of time to get it finished. if you look at a website called brightpanel.com.au the products shown on this website are what we want to show on the shop front. each product is to have a pricing star or symbol next to it so We can add pricing later. I will include a photos of the shop front the signage area sizes are as follows: 1 x 4290 x 1200, 1 x 8930 x 1200, 1 x 6280 x 1200 . We will be printing the design on media and applying to 3mm ACM 2400 X 1200 sheeting. design to be format in AI and printable PDF and in CMYK colours with a 10mm bleed border all round. wanting a high impact design based around our logo and colour branding Green/Blue, must be easy to read from a street approx 6 metres away. logo attached , photo of elevation attached , part complete design attached . We are wanting a panel also dedicated to printing i.e business cards 250 card on 350gsm $77, leaflets , calendars , catalogues supply etc .

Target Market(s)

Passing traffic

Font styles to use
Sans Serif

Colors
9bcb3b

Requirements
Must have
• Impact , easy to read, pricing
Nice to have
• nice clear images
Should not have
• any image with bad pix-elation

```html
<!DOCTYPE html>
<html lang="en">
<head>
<meta charset="utf-8">
<title>Marlow Signs – Shop Front Signage</title>
<link rel="stylesheet" href="https://fonts.googleapis.com/css2?family=Oswald:wght@300;400;500;600&family=Open+Sans:wght@800&display=swap">
<style>
:root{
  --green:#9bcb3b;
  --green-mid:#7dc242;
  --green-deep:#5bb547;
  --teal:#2fb39b;
  --blue:#1ba9d6;
  --band:#8dc63f;
  --white:#ffffff;
  --ink:#2b2b2b;
}
*{margin:0;padding:0;box-sizing:border-box}
html,body{width:1200px;height:1056px;overflow:hidden}
body{background:radial-gradient(ellipse at 50% 45%,#f2f2f2 0%,#d9d9d9 60%,#bdbdbd 100%);font-family:"Oswald",sans-serif;position:relative}
.size-label{position:absolute;left:86px;font:300 28px/1 "Oswald",sans-serif;color:var(--ink)}
.banner{position:absolute;left:86px;width:1028px;overflow:hidden;background:var(--white);box-shadow:0 16px 18px -12px rgba(0,0,0,.4)}
.banner svg.bg{position:absolute;inset:0}
.title{position:absolute;color:var(--white);font-weight:400;line-height:1;padding:4px 14px 6px 12px;border-radius:8px;background:rgba(0,0,0,.06);box-shadow:0 2px 4px rgba(0,0,0,.08)}
.svc{position:absolute;display:flex;align-items:center;gap:7px;color:var(--white);font-weight:500;line-height:1;white-space:nowrap;text-shadow:0 1px 2px rgba(0,0,0,.2)}
.svc svg{flex:none}
.phone{position:absolute;display:flex;align-items:center;gap:6px;color:var(--white);font-family:"Open Sans",sans-serif;font-weight:800;line-height:1;text-shadow:0 1px 2px rgba(0,0,0,.15)}
.web{position:absolute;display:flex;align-items:center;gap:8px;color:var(--white);font-weight:300;line-height:1}
.brand{position:absolute;text-align:center;color:var(--green-deep);font-weight:600;line-height:1;letter-spacing:.5px;white-space:nowrap;transform:translateX(-50%)}
</style>
</head>
<body>

<div class="size-label" style="top:56px">4290 by 1200</div>
<section class="banner" style="top:98px;height:287px">
  <svg class="bg" width="1028" height="287" viewBox="0 0 1028 287">
    <defs>
      <linearGradient id="p1" x1="0" y1="1" x2="1" y2="0"><stop offset="0" stop-color="#8cc63f"/><stop offset=".5" stop-color="#5fbf5a"/><stop offset="1" stop-color="#2aae96"/></linearGradient>
      <linearGradient id="r1" x1="0" y1="0" x2="1" y2="1"><stop offset="0" stop-color="#6cc04a"/><stop offset="1" stop-color="#20ade0"/></linearGradient>
    </defs>
    <path d="M386,0 Q345,140 370,235 L1028,235 L1028,0 Z" fill="url(#p1)"/>
    <rect x="0" y="232" width="1028" height="55" fill="var(--band)"/>
    <rect x="0" y="232" width="1028" height="3" fill="#a8d65a"/>
    <path d="M1028,8 Q925,110 985,287 L1028,287 Z" fill="#8cc63f" opacity=".85"/>
    <circle cx="178" cy="142" r="152" fill="#fff" stroke="url(#r1)" stroke-width="6"/>
  </svg>
  <div class="brand" style="left:178px;top:128px;font-size:30px">MARLOW SIGNS</div>
  <div class="title" style="left:407px;top:46px;font-size:29px">Sign And Print Centre</div>
  <div class="svc" style="left:412px;top:112px;font-size:31px"><svg width="26" height="26" viewBox="0 0 26 26"><path d="M3 4h18l3 3-3 3H3z M11 10h3v15h-3z" fill="#fff"/></svg>Signs</div>
  <div class="svc" style="left:412px;top:156px;font-size:31px"><svg width="26" height="26" viewBox="0 0 26 26"><path d="M13 2a11 11 0 1 0 11 11H13z" fill="#fff"/><path d="M15 0v11h11A11 11 0 0 0 15 0z" fill="#fff"/></svg>Stickers and Decals</div>
  <div class="svc" style="left:710px;top:112px;font-size:31px"><svg width="26" height="26" viewBox="0 0 26 26"><path d="M3 3l20 20M23 3L3 23" stroke="#fff" stroke-width="3"/></svg>Graphics Design</div>
  <div class="svc" style="left:710px;top:156px;font-size:31px"><svg width="30" height="22" viewBox="0 0 30 22"><path d="M2 4h18v12H2z M20 8h5l3 4v4h-8z" fill="none" stroke="#fff" stroke-width="2.5"/><circle cx="8" cy="18" r="3" fill="#fff"/><circle cx="23" cy="18" r="3" fill="#fff"/></svg>Vehicle Wraps</div>
  <div class="phone" style="left:403px;top:244px;font-size:34px"><svg width="10" height="26" viewBox="0 0 10 26"><path d="M8 2C2 6 2 20 8 24" stroke="#fff" stroke-width="4" fill="none"/></svg>9000 4127</div>
  <div class="web" style="left:602px;top:246px;font-size:27px"><svg width="18" height="18" viewBox="0 0 18 18"><circle cx="9" cy="9" r="8" fill="#fff"/><path d="M1 9h16M9 1v16M3 5h12M3 13h12" stroke="var(--band)" stroke-width="1.2"/></svg>www.marlowsigns.com.au</div>
</section>

<div class="size-label" style="top:450px">6280 by 1200</div>
<section class="banner" style="top:496px;height:196px">
  <svg class="bg" width="1028" height="196" viewBox="0 0 1028 196">
    <defs>
      <linearGradient id="p2" x1="0" y1="1" x2="1" y2="0"><stop offset="0" stop-color="#8cc63f"/><stop offset=".5" stop-color="#5fbf5a"/><stop offset="1" stop-color="#2aae96"/></linearGradient>
      <linearGradient id="r2" x1="0" y1="0" x2="1" y2="1"><stop offset="0" stop-color="#6cc04a"/><stop offset="1" stop-color="#20ade0"/></linearGradient>
    </defs>
    <path d="M282,0 Q258,90 270,144 L1028,144 L1028,0 Z" fill="url(#p2)"/>
    <rect x="0" y="142" width="1028" height="54" fill="var(--band)"/>
    <rect x="0" y="142" width="1028" height="3" fill="#a8d65a"/>
    <path d="M1028,4 Q945,80 1000,196 L1028,196 Z" fill="#8cc63f" opacity=".85"/>
    <circle cx="133" cy="98" r="108" fill="#fff" stroke="url(#r2)" stroke-width="5"/>
  </svg>
  <div class="brand" style="left:133px;top:86px;font-size:23px">MARLOW SIGNS</div>
  <div class="title" style="left:318px;top:14px;font-size:26px">Sign And Print Centre</div>
  <div class="svc" style="left:318px;top:64px;font-size:27px"><svg width="16" height="20" viewBox="0 0 16 20"><rect x="1" y="1" width="14" height="18" fill="none" stroke="#fff" stroke-width="2"/><rect x="4" y="4" width="8" height="9" fill="#fff"/></svg>Wide Format Posters</div>
  <div class="svc" style="left:318px;top:102px;font-size:27px"><svg width="16" height="18" viewBox="0 0 16 18"><rect x="1" y="1" width="14" height="16" fill="none" stroke="#fff" stroke-width="2"/><path d="M4 6h8M4 10h8" stroke="#fff" stroke-width="2"/></svg>Banners</div>
  <div class="svc" style="left:590px;top:64px;font-size:27px"><svg width="24" height="18" viewBox="0 0 24 18"><path d="M0 1h24M0 6h24M0 11h24M0 16h24M6 1v5M16 1v5M11 6v5M20 6v5M6 11v5M16 11v5" stroke="#fff" stroke-width="2"/></svg>Wall graphics</div>
  <div class="svc" style="left:590px;top:102px;font-size:27px"><svg width="26" height="20" viewBox="0 0 26 20"><rect x="1" y="5" width="22" height="13" fill="#fff"/><path d="M4 1h20v12" fill="none" stroke="#fff" stroke-width="2"/></svg>Business Cards &amp; Stationery</div>
  <div class="phone" style="left:314px;top:155px;font-size:34px"><svg width="10" height="26" viewBox="0 0 10 26"><path d="M8 2C2 6 2 20 8 24" stroke="#fff" stroke-width="4" fill="none"/></svg>9000 4127</div>
  <div class="web" style="left:533px;top:157px;font-size:27px"><svg width="18" height="18" viewBox="0 0 18 18"><circle cx="9" cy="9" r="8" fill="#fff"/><path d="M1 9h16M9 1v16M3 5h12M3 13h12" stroke="var(--band)" stroke-width="1.2"/></svg>www.marlowsigns.com.au</div>
</section>

<div class="size-label" style="top:774px">8930 by 1200</div>
<section class="banner" style="top:819px;height:138px">
  <svg class="bg" width="1028" height="138" viewBox="0 0 1028 138">
    <defs>
      <linearGradient id="p3" x1="0" y1="1" x2="1" y2="0"><stop offset="0" stop-color="#8cc63f"/><stop offset=".45" stop-color="#4fbb6a"/><stop offset="1" stop-color="#1aa8d8"/></linearGradient>
      <linearGradient id="r3" x1="0" y1="0" x2="1" y2="1"><stop offset="0" stop-color="#6cc04a"/><stop offset="1" stop-color="#20ade0"/></linearGradient>
    </defs>
    <path d="M250,0 Q230,60 240,101 L1028,101 L1028,0 Z" fill="url(#p3)"/>
    <rect x="0" y="99" width="1028" height="39" fill="var(--band)"/>
    <rect x="0" y="99" width="1028" height="3" fill="#a8d65a"/>
    <path d="M1028,2 Q975,55 1010,138 L1028,138 Z" fill="#8cc63f" opacity=".85"/>
    <circle cx="118" cy="69" r="95" fill="#fff" stroke="url(#r3)" stroke-width="4"/>
  </svg>
  <div class="brand" style="left:118px;top:60px;font-size:19px">MARLOW SIGNS</div>
  <div class="title" style="left:280px;top:15px;font-size:22px">Sign And Print Centre</div>
  <div class="svc" style="left:271px;top:58px;font-size:28px"><svg width="26" height="18" viewBox="0 0 26 18"><path d="M2 9l4-7h14l4 7v7H2z" fill="#fff"/><rect x="7" y="4" width="12" height="5" fill="var(--teal)"/></svg>Vehicle Signs</div>
  <div class="svc" style="left:477px;top:58px;font-size:28px"><svg width="28" height="18" viewBox="0 0 28 18"><rect x="1" y="1" width="26" height="16" fill="none" stroke="#fff" stroke-width="2"/><text x="14" y="14" font-family="Oswald,sans-serif" font-size="12" font-weight="600" fill="#fff" text-anchor="middle">3D</text></svg>3D Signage</div>
  <div class="svc" style="left:662px;top:58px;font-size:28px"><svg width="20" height="20" viewBox="0 0 20 20"><path d="M10 2l3 6H7z M4 12h12M1 18h18" stroke="#fff" stroke-width="2" fill="#fff"/></svg>Pylon Signage</div>
  <div class="svc" style="left:871px;top:58px;font-size:28px"><svg width="18" height="22" viewBox="0 0 18 22"><rect x="1" y="1" width="16" height="20" fill="none" stroke="#fff" stroke-width="2"/><circle cx="7" cy="7" r="3" fill="#fff"/><path d="M4 13h10M4 17h10" stroke="#fff" stroke-width="2"/></svg>Flyers</div>
  <div class="phone" style="left:348px;top:106px;font-size:29px"><svg width="9" height="22" viewBox="0 0 10 26"><path d="M8 2C2 6 2 20 8 24" stroke="#fff" stroke-width="4" fill="none"/></svg>9000 4127</div>
  <div class="web" style="left:549px;top:108px;font-size:23px"><svg width="16" height="16" viewBox="0 0 18 18"><circle cx="9" cy="9" r="8" fill="#fff"/><path d="M1 9h16M9 1v16M3 5h12M3 13h12" stroke="var(--band)" stroke-width="1.2"/></svg>www.marlowsigns.com.au</div>
</section>

</body>
</html>
```